Re-drawing and gpahically, according to coorporate design

Three flowcharts need to be re-drawn and graphically improved according to coorporate design

```html
<!DOCTYPE html>
<html lang="en">
<head>
<meta charset="utf-8">
<title>Auenfeld Energy Institute – Carbon and Hydrogen Pathways</title>
<link href="https://fonts.googleapis.com/css2?family=Open+Sans:wght@400;600;700&display=swap" rel="stylesheet">
<style>
  :root{
    --slate:#5a7b79;
    --olive:#b3b013;
    --olive-dark:#98960f;
    --band:#899b3b;
    --grey:#6d7372;
    --ink:#1c1c1c;
    --paper:#ffffff;
  }
  html,body{margin:0;padding:0;overflow:hidden;background:var(--paper);}
  .canvas{width:985px;height:1200px;position:relative;overflow:hidden;}
  .canvas svg{display:block;width:985px;height:1200px;font-family:'Open Sans',sans-serif;}
  .bar{fill:var(--slate);}
  .band{fill:var(--band);}
  .box{fill:var(--slate);}
  .node{fill:var(--olive);stroke:var(--olive-dark);stroke-width:2;}
  .node-ring{fill:none;stroke:#fff;stroke-width:1.2;opacity:.8;}
  .flow-olive{fill:none;stroke:var(--olive);stroke-width:3;}
  .flow-slate{fill:none;stroke:var(--slate);stroke-width:3;}
  .flow-grey{fill:none;stroke:var(--grey);stroke-width:3;}
  .label{fill:#fff;font-weight:700;text-anchor:middle;}
  .brand-name{fill:var(--ink);font-weight:600;font-size:30px;}
  .brand-sub{fill:var(--ink);font-weight:600;font-size:13px;}
  .list-item{fill:var(--slate);font-size:15px;font-weight:400;}
  .partner-frame{fill:#fff;stroke:var(--olive);stroke-width:3;}
  .partner-badge{fill:#d9dfde;}
</style>
</head>
<body>
<div class="canvas">
<svg viewBox="0 0 1080 1316" xmlns="http://www.w3.org/2000/svg">
  <defs>
    <marker id="head-olive" viewBox="0 0 10 10" refX="8" refY="5" markerWidth="5" markerHeight="5" orient="auto">
      <polyline points="1,1 8,5 1,9" fill="none" stroke="#b3b013" stroke-width="2.2"/>
    </marker>
    <marker id="head-slate" viewBox="0 0 10 10" refX="8" refY="5" markerWidth="5" markerHeight="5" orient="auto">
      <polyline points="1,1 8,5 1,9" fill="none" stroke="#5a7b79" stroke-width="2.2"/>
    </marker>
    <marker id="head-grey" viewBox="0 0 10 10" refX="8" refY="5" markerWidth="5" markerHeight="5" orient="auto">
      <polyline points="1,1 8,5 1,9" fill="none" stroke="#6d7372" stroke-width="2.2"/>
    </marker>
  </defs>

  <!-- header brand -->
  <g class="brand">
    <circle cx="176" cy="121" r="30" fill="none" stroke="#1c1c1c" stroke-width="3"/>
    <text class="brand-name" x="216" y="114">AUENFELD</text>
    <text class="brand-name" x="216" y="148">ENERGY INSTITUTE</text>
    <text class="brand-sub" x="145" y="168">Auenfeld Energy Institute</text>
  </g>

  <rect class="bar" x="110" y="212" width="859" height="14"/>
  <rect class="bar" x="110" y="1091" width="859" height="14"/>
  <rect class="band" x="0" y="1188" width="1080" height="128"/>

  <!-- origin idea node -->
  <g class="origin">
    <path d="M195 271 A66 66 0 0 1 258 318 L268 337 L258 356 A66 66 0 0 1 211 401 L195 412 L179 401 A66 66 0 0 1 195 271 Z" fill="var(--olive)"/>
    <circle cx="195" cy="337" r="55" fill="var(--slate)"/>
    <g class="icon-bulb" fill="#fff">
      <circle cx="195" cy="324" r="24"/>
      <rect x="184" y="340" width="22" height="12" rx="2"/>
      <rect x="185" y="354" width="20" height="4" rx="2"/>
      <rect x="187" y="361" width="16" height="4" rx="2"/>
    </g>
  </g>

  <!-- left chain: electricity to hydrogen -->
  <line class="flow-olive" x1="268" y1="337" x2="362" y2="337" marker-end="url(#head-olive)"/>
  <line class="flow-olive" x1="195" y1="412" x2="195" y2="456" marker-end="url(#head-olive)"/>
  <circle class="node" cx="195" cy="508" r="39"/><circle class="node-ring" cx="195" cy="508" r="34"/>
  <text class="label" x="195" y="507" font-size="11">Renewable</text>
  <text class="label" x="195" y="521" font-size="11">Electricity</text>
  <line class="flow-olive" x1="195" y1="547" x2="195" y2="612" marker-end="url(#head-olive)"/>
  <rect class="box" x="147" y="625" width="98" height="47" rx="4"/>
  <text class="label" x="196" y="653" font-size="13">Electrolysis</text>
  <line class="flow-slate" x1="195" y1="672" x2="195" y2="746" marker-end="url(#head-slate)"/>
  <circle class="node" cx="195" cy="786" r="28"/><circle class="node-ring" cx="195" cy="786" r="24"/>
  <text class="label" x="195" y="791" font-size="13">H₂</text>
  <line class="flow-olive" x1="195" y1="814" x2="195" y2="879" marker-end="url(#head-olive)"/>
  <polyline class="flow-olive" points="223,786 291,786 291,864 318,864" marker-end="url(#head-olive)"/>
  <rect class="box" x="147" y="894" width="95" height="64" rx="4"/>
  <text class="label" x="195" y="916" font-size="13">Various</text>
  <text class="label" x="195" y="932" font-size="13">Direct</text>
  <text class="label" x="195" y="948" font-size="13">Applications</text>
  <path d="M147 963 H242 V1024 Q242 1032 234 1032 H155 Q147 1032 147 1024 Z" fill="#fff" stroke="var(--slate)" stroke-width="3"/>
  <g class="list-item">
    <circle cx="162" cy="980" r="3" fill="var(--slate)"/><text x="171" y="986">Mobility</text>
    <circle cx="162" cy="995" r="3" fill="var(--slate)"/><text x="171" y="1001">Industry</text>
    <circle cx="162" cy="1010" r="3" fill="var(--slate)"/><text x="171" y="1016">Gas Grid</text>
  </g>

  <!-- biomass chain -->
  <rect class="box" x="381" y="314" width="150" height="44" rx="4"/>
  <text class="label" x="456" y="333" font-size="13">Agriculture/</text>
  <text class="label" x="456" y="349" font-size="13">Forestry</text>
  <line class="flow-slate" x1="531" y1="336" x2="581" y2="336" marker-end="url(#head-slate)"/>
  <rect class="box" x="595" y="314" width="150" height="44" rx="4"/>
  <text class="label" x="669" y="341" font-size="13">Industry</text>
  <polyline class="flow-slate" points="745,337 818,337"/>
  <line class="flow-slate" x1="818" y1="302" x2="818" y2="368"/>
  <line class="flow-slate" x1="818" y1="302" x2="873" y2="302" marker-end="url(#head-slate)"/>
  <line class="flow-slate" x1="818" y1="368" x2="873" y2="368" marker-end="url(#head-slate)"/>
  <circle class="node" cx="915" cy="302" r="29"/><circle class="node-ring" cx="915" cy="302" r="25"/>
  <text class="label" x="915" y="305" font-size="8.5">Food/feed</text>
  <circle class="node" cx="915" cy="368" r="29"/><circle class="node-ring" cx="915" cy="368" r="25"/>
  <text class="label" x="915" y="358" font-size="8.5">Wood</text>
  <text class="label" x="915" y="369" font-size="8.5">Based</text>
  <text class="label" x="915" y="380" font-size="8.5">Products</text>

  <polyline class="flow-slate" points="457,358 457,442 520,442" marker-end="url(#head-slate)"/>
  <polyline class="flow-slate" points="669,358 669,442 619,442" marker-end="url(#head-slate)"/>
  <circle class="node" cx="568" cy="443" r="32"/><circle class="node-ring" cx="568" cy="443" r="28"/>
  <text class="label" x="568" y="447" font-size="11">Residues</text>

  <line class="flow-olive" x1="568" y1="475" x2="568" y2="498"/>
  <line class="flow-olive" x1="464" y1="498" x2="666" y2="498"/>
  <line class="flow-olive" x1="464" y1="498" x2="464" y2="535" marker-end="url(#head-olive)"/>
  <line class="flow-olive" x1="568" y1="498" x2="568" y2="535" marker-end="url(#head-olive)"/>
  <line class="flow-olive" x1="666" y1="498" x2="666" y2="535" marker-end="url(#head-olive)"/>

  <rect class="box" x="425" y="549" width="84" height="68" rx="4"/>
  <text class="label" x="467" y="579" font-size="10">Anaerobic</text>
  <text class="label" x="467" y="591" font-size="10">Digestion</text>
  <rect class="box" x="528" y="549" width="76" height="68" rx="4"/>
  <text class="label" x="566" y="580" font-size="10">Biomass</text>
  <text class="label" x="566" y="592" font-size="10">Gastification</text>
  <rect class="box" x="624" y="549" width="83" height="68" rx="4"/>
  <text class="label" x="666" y="585" font-size="10">Fermentation</text>

  <line class="flow-grey" x1="425" y1="580" x2="367" y2="580" marker-end="url(#head-grey)"/>
  <rect class="box" x="279" y="521" width="96" height="18" rx="2"/>
  <text class="label" x="327" y="534" font-size="9.5">Cleaner Gas Route</text>
  <circle class="node" cx="323" cy="583" r="29"/><circle class="node-ring" cx="323" cy="583" r="25"/>
  <text class="label" x="323" y="589" font-size="15">CH</text>

  <line class="flow-slate" x1="707" y1="582" x2="818" y2="582"/>
  <line class="flow-slate" x1="818" y1="513" x2="818" y2="650"/>
  <line class="flow-slate" x1="818" y1="513" x2="873" y2="513" marker-end="url(#head-slate)"/>
  <line class="flow-slate" x1="818" y1="582" x2="873" y2="582" marker-end="url(#head-slate)"/>
  <line class="flow-slate" x1="818" y1="650" x2="873" y2="650" marker-end="url(#head-slate)"/>
  <circle class="node" cx="915" cy="511" r="29"/><circle class="node-ring" cx="915" cy="511" r="25"/>
  <text class="label" x="915" y="514" font-size="8.5">Chemicals</text>
  <circle class="node" cx="915" cy="580" r="29"/><circle class="node-ring" cx="915" cy="580" r="25"/>
  <text class="label" x="915" y="583" font-size="8.5">Polymers</text>
  <circle class="node" cx="915" cy="650" r="29"/><circle class="node-ring" cx="915" cy="650" r="25"/>
  <text class="label" x="915" y="653" font-size="8.5">Fuels</text>

  <polyline class="flow-slate" points="465,617 465,653 532,653 546,678" marker-end="url(#head-slate)"/>
  <line class="flow-slate" x1="566" y1="617" x2="566" y2="680" marker-end="url(#head-slate)"/>
  <polyline class="flow-slate" points="664,617 664,653 598,653 585,678" marker-end="url(#head-slate)"/>

  <circle class="node" cx="565" cy="716" r="29"/><circle class="node-ring" cx="565" cy="716" r="25"/>
  <text class="label" x="565" y="721" font-size="13">CO₂</text>

  <!-- conversion routes -->
  <line class="flow-olive" x1="565" y1="745" x2="565" y2="779"/>
  <line class="flow-olive" x1="368" y1="779" x2="758" y2="779"/>
  <line class="flow-olive" x1="368" y1="779" x2="368" y2="823" marker-end="url(#head-olive)"/>
  <line class="flow-olive" x1="465" y1="779" x2="465" y2="823" marker-end="url(#head-olive)"/>
  <line class="flow-olive" x1="565" y1="779" x2="565" y2="823" marker-end="url(#head-olive)"/>
  <line class="flow-olive" x1="661" y1="779" x2="661" y2="823" marker-end="url(#head-olive)"/>
  <line class="flow-olive" x1="758" y1="779" x2="758" y2="823" marker-end="url(#head-olive)"/>

  <rect class="box" x="331" y="834" width="75" height="69" rx="4"/>
  <text class="label" x="368" y="858" font-size="9.5">Electro-</text>
  <text class="label" x="368" y="869" font-size="9.5">Chemical</text>
  <text class="label" x="368" y="880" font-size="9.5">Conversion</text>
  <rect class="box" x="428" y="834" width="75" height="69" rx="4"/>
  <text class="label" x="465" y="858" font-size="9.5">Catalytic/</text>
  <text class="label" x="465" y="869" font-size="9.5">Biological</text>
  <text class="label" x="465" y="880" font-size="9.5">Methanation</text>
  <rect class="box" x="526" y="834" width="75" height="69" rx="4"/>
  <text class="label" x="563" y="853" font-size="9.5">Other</text>
  <text class="label" x="563" y="864" font-size="9.5">Chemical</text>
  <text class="label" x="563" y="876" font-size="9.5">Trans-</text>
  <text class="label" x="563" y="887" font-size="9.5">formation</text>
  <rect class="box" x="623" y="834" width="75" height="69" rx="4"/>
  <text class="label" x="660" y="858" font-size="9.5">Existing</text>
  <text class="label" x="660" y="869" font-size="9.5">Industrial</text>
  <text class="label" x="660" y="880" font-size="9.5">Applications</text>
  <rect class="box" x="721" y="834" width="75" height="69" rx="4"/>
  <text class="label" x="758" y="871" font-size="10">Algea</text>

  <line class="flow-slate" x1="368" y1="903" x2="368" y2="951" marker-end="url(#head-slate)"/>
  <line class="flow-slate" x1="465" y1="903" x2="465" y2="951" marker-end="url(#head-slate)"/>
  <line class="flow-slate" x1="565" y1="903" x2="565" y2="951" marker-end="url(#head-slate)"/>
  <line class="flow-slate" x1="661" y1="903" x2="661" y2="951" marker-end="url(#head-slate)"/>
  <line class="flow-slate" x1="758" y1="903" x2="758" y2="951" marker-end="url(#head-slate)"/>

  <rect class="partner-badge" x="385" y="932" width="58" height="16" rx="3"/>
  <rect class="partner-badge" x="675" y="924" width="58" height="20" rx="3"/>

  <circle class="node" cx="368" cy="988" r="27"/><circle class="node-ring" cx="368" cy="988" r="23"/>
  <text class="label" x="368" y="991" font-size="8">CH₄</text>
  <circle class="node" cx="466" cy="988" r="28"/><circle class="node-ring" cx="466" cy="988" r="24"/>
  <text class="label" x="466" y="976" font-size="7.5">e.g.</text>
  <text class="label" x="466" y="985" font-size="7.5">Ethylen-</text>
  <text class="label" x="466" y="994" font-size="7.5">Oxide</text>
  <text class="label" x="466" y="1003" font-size="7.5">C₂H₄O</text>
  <circle class="node" cx="565" cy="988" r="28"/><circle class="node-ring" cx="565" cy="988" r="24"/>
  <text class="label" x="565" y="976" font-size="7.5">e.g.</text>
  <text class="label" x="565" y="985" font-size="7.5">Polyol,</text>
  <text class="label" x="565" y="994" font-size="7.5">Polymel,</text>
  <text class="label" x="565" y="1003" font-size="7.5">Etc...</text>
  <circle class="node" cx="661" cy="988" r="29"/><circle class="node-ring" cx="661" cy="988" r="25"/>
  <text class="label" x="661" y="980" font-size="7.5">e.g.</text>
  <text class="label" x="661" y="989" font-size="7.5">Beverage</text>
  <text class="label" x="661" y="998" font-size="7.5">Industry</text>
  <circle class="node" cx="758" cy="988" r="29"/><circle class="node-ring" cx="758" cy="988" r="25"/>
  <text class="label" x="758" y="987" font-size="8">Fuel, Bio-</text>
  <text class="label" x="758" y="997" font-size="8">Polymers</text>

  <!-- partner projects -->
  <rect class="partner-frame" x="831" y="722" width="113" height="310"/>
  <g class="partners">
    <rect class="partner-badge" x="846" y="743" width="80" height="24" rx="3"/>
    <rect class="partner-badge" x="846" y="778" width="78" height="24" rx="3"/>
    <rect class="partner-badge" x="846" y="806" width="78" height="28" rx="3"/>
    <rect class="partner-badge" x="846" y="838" width="78" height="20" rx="3"/>
    <rect class="partner-badge" x="846" y="868" width="84" height="28" rx="3"/>
    <rect class="partner-badge" x="846" y="906" width="84" height="22" rx="3"/>
    <rect class="partner-badge" x="846" y="936" width="84" height="38" rx="3"/>
    <rect class="partner-badge" x="846" y="982" width="84" height="32" rx="3"/>
  </g>
</svg>
</div>
</body>
</html>
```